Redesign for Popular UK Town Website

We're looking for someone to redesign a website for a popular tourist town that's visited by over 250,000 people a year. We have a basic design frame in place and need someone to make it look more 'professional.'
We've created a temporary design layout to show you a general idea of what we're looking for: http://dorrin.co.uk/
All text/images are placeholder images so you can get an idea of the general layout.
(Please note that you can grab any images found on the internet for 'tenby' to be used as placeholder images. This is because we will be visiting the locations and taking our own photos, after the design is complete.)
Target Market(s)
Tourists
Industry/Entity Type
Town
Number of Pages Required
2 page
Requirements
Must have
- You need to redesign the homepage: http://dorrin.co.uk/
- You also need to redesign the following page: http://dorrin.co.uk/hotels/ (This page will be used for multiple categories and is used to list locations of properties/places etc.)
- Design must be responsive also.
Nice to have
- Please feel free to add as much as you can to the content/features as with our limited knowledge of websites, have only been able to create a basic layout.

```html
<!DOCTYPE html>
<html lang="en">
<head>
<meta charset="utf-8">
<title>Dorrin – Welcome</title>
<link rel="stylesheet" href="https://fonts.googleapis.com/css2?family=Kaushan+Script&family=Saira+Condensed:wght@600;700&family=Rajdhani:wght@500;600;700&family=Lato:wght@300;400;700&display=swap">
<style>
:root{
  --sky:#1aa3e8;
  --sky-dark:#0b78c2;
  --navy:#0d3f63;
  --ink:#1d4f78;
  --text:#555c63;
  --muted:#8a9299;
  --ghost:#e6ecf1;
  --paper:#ffffff;
}
*{box-sizing:border-box;margin:0;padding:0}
html,body{width:1200px;height:3025px;overflow:hidden;background:var(--paper)}
body{position:relative;font-family:'Lato',sans-serif;color:var(--text)}
.abs{position:absolute}

/* hero */
.hero{left:0;top:0;width:1200px;height:555px;
  background:linear-gradient(180deg,#8fb3cf 0%,#6e8fa6 30%,#4b6478 55%,#2f4250 80%,#24323c 100%)}
.topbar-band{left:0;top:0;width:1200px;height:60px;background:linear-gradient(90deg,#ffffff 0%,#ffffff 18%,var(--sky) 28%,var(--sky-dark) 100%);opacity:.95}
.brand{left:30px;top:14px;display:flex;align-items:center;gap:8px;font-family:'Saira Condensed',sans-serif;font-weight:700;font-size:22px;color:var(--sky-dark);letter-spacing:.5px}
.brand-dot{width:30px;height:30px;border-radius:50%;background:var(--sky-dark)}
.nav{right:40px;top:22px;display:flex;gap:34px;font-family:'Rajdhani',sans-serif;font-weight:700;font-size:13px;letter-spacing:1.2px;color:#fff;text-transform:uppercase}
.hero-title{left:131px;top:200px;font-family:'Kaushan Script',cursive;font-size:62px;font-weight:400;color:#fff}
.hero-copy{left:131px;top:292px;width:640px;font-family:'Rajdhani',sans-serif;font-weight:600;font-size:15px;line-height:28px;color:#fff}
.btn{display:flex;align-items:center;justify-content:center;background:var(--sky);color:#fff;font-family:'Lato',sans-serif;font-weight:700;letter-spacing:2px;text-transform:uppercase}
.hero-btn{left:133px;top:434px;width:200px;height:38px;font-size:14px}

/* categories */
.cat{top:631px;width:165px;height:222px;text-align:center}
.cat.active{background:linear-gradient(180deg,var(--sky) 0%,var(--sky-dark) 60%,var(--navy) 100%);color:#fff}
.cat svg{display:block;margin:24px auto 0}
.cat-name{margin-top:14px;font-family:'Rajdhani',sans-serif;font-weight:600;font-size:14px;letter-spacing:1px;color:var(--ink)}
.cat.active .cat-name{color:#fff}
.cat-rule{width:52px;height:1px;background:#fff;margin:12px auto 0}
.cat-desc{margin-top:14px;font-size:11.5px;line-height:14px;color:var(--muted)}
.cat.active .cat-desc{color:#fff}

/* section headings */
.ghost{left:0;width:1200px;text-align:center;font-family:'Kaushan Script',cursive;font-size:130px;color:var(--ghost);line-height:1}
.heading{left:0;width:1200px;text-align:center;font-family:'Saira Condensed',sans-serif;font-weight:700;font-size:38px;letter-spacing:1px;color:var(--ink)}

/* things to do */
.card{top:1119px;width:464px;height:330px;background:#fff;box-shadow:0 4px 22px rgba(0,0,0,.12)}
.card-img{left:0;top:0;width:222px;height:330px}
.badge{left:0;top:0;width:38px;height:38px;background:var(--sky);color:#fff;border-bottom-right-radius:22px;font-family:'Kaushan Script',cursive;font-size:20px;padding:2px 0 0 8px}
.card-title{left:248px;top:30px;width:200px;font-size:20px;font-weight:400;line-height:25px;color:#222}
.card-copy{left:248px;top:112px;width:196px;font-size:11.5px;line-height:20px;color:var(--muted)}
.card-link{left:248px;top:283px;font-size:11.5px;font-weight:700;color:var(--sky)}
.arrow{top:1270px}
.view-all{left:496px;top:1500px;width:182px;height:38px;font-size:12px;letter-spacing:3px}

/* dining */
.dine-img{left:67px;top:1815px;width:633px;height:585px;background:radial-gradient(ellipse at 45% 65%,#7a5a3c 0%,#4a3626 35%,#2a211b 70%,#1b1613 100%)}
.dots{left:100px;top:2362px;display:flex;gap:10px}
.dots span{width:12px;height:12px;border-radius:50%;border:2px solid #fff}
.dots span:first-child{background:#fff}
.dine-card{left:700px;top:1815px;width:436px;height:585px;background:#fff;box-shadow:0 4px 22px rgba(0,0,0,.12)}
.dine-title{left:32px;top:55px;font-family:'Saira Condensed',sans-serif;font-weight:700;font-size:34px;color:var(--ink)}
.tags{left:32px;top:120px;width:385px;display:flex;flex-wrap:wrap;gap:12px 10px}
.tag{border:1px solid #333;border-radius:18px;padding:8px 14px;font-size:11px;color:#333}
.dine-copy{left:32px;top:270px;width:385px;font-size:11px;line-height:21px;color:var(--muted)}
.dine-copy p+p{margin-top:18px}
.pager{top:482px;font-size:12px;letter-spacing:1px}
.prev{left:32px;color:var(--muted)}
.next{right:32px;color:var(--sky);font-weight:700}

/* hotels */
.hotel-img{top:2699px;height:139px}
.hotel-card{left:319px;top:2667px;width:310px;height:201px;background:linear-gradient(135deg,var(--sky) 0%,var(--sky-dark) 100%);color:#fff;box-shadow:0 6px 20px rgba(0,0,0,.2)}
.hotel-name{left:24px;top:22px;font-family:'Rajdhani',sans-serif;font-weight:700;font-size:17px;letter-spacing:2px}
.hotel-rule{left:24px;top:54px;width:262px;height:1px;background:rgba(255,255,255,.7)}
.hotel-info{left:24px;top:78px;font-size:10.5px;line-height:22px;list-style:none}
.hotel-info li{display:flex;align-items:center;gap:10px}
.hotel-book{left:24px;top:162px;font-size:12px;font-weight:700;letter-spacing:2px}
.hotel-detail{left:176px;top:152px;width:114px;height:34px;background:#fff;color:var(--sky);font-size:11px}

/* footer */
.footer{left:0;top:2945px;width:1200px;height:80px;background:var(--navy)}
.footer .brand{left:64px;top:24px;color:#fff}
.footer .brand-dot{background:#fff}
.copyright{right:70px;top:32px;font-size:12.5px;color:#fff}
</style>
</head>
<body>

<header>
  <div class="abs hero" role="img" aria-label="Photo of the harbour town with colourful houses above boats in the bay"></div>
  <div class="abs topbar-band"></div>
  <div class="abs brand"><span class="brand-dot"></span>DORRIN.CO.UK</div>
  <nav class="abs nav"><span>Where to stay</span><span>Caravan and camping</span><span>Bed and breakfast</span><span>Hotels in Dorrin</span></nav>
  <h1 class="abs hero-title">Welcome to Dorrin.</h1>
  <p class="abs hero-copy">The jewel in the crown of Westmorrow. A popular harbour town visited by<br>over 299,000 visitors a year. Surrounded by its medieval stone wall, Dorrin is steeped with history and beautiful landscapes. Famed for it's beautiful beaches and views that will lure you to come back each year, we hope you enjoy your time visting and breathing in the sea air of Dorrin.</p>
  <a class="abs btn hero-btn">Explore city</a>
</header>

<section class="categories">
  <div class="abs cat" style="left:200px">
    <svg width="40" height="44" viewBox="0 0 40 44" fill="none" stroke="#333" stroke-width="1.5"><rect x="8" y="6" width="24" height="34"/><path d="M2 6h36M14 6v10h12V6"/></svg>
    <div class="cat-name">Hotels in Dorrin</div>
    <div class="cat-desc">Where to stay<br>hotel, apartment, hostel,<br>guest house</div>
  </div>
  <div class="abs cat active" style="left:355px">
    <svg width="52" height="44" viewBox="0 0 52 44" fill="none" stroke="#fff" stroke-width="1.5"><path d="M6 36L26 6l20 30zM26 6v30M2 40h48"/><path d="M20 36l6-10 6 10"/></svg>
    <div class="cat-name">Caravan and camping</div>
    <div class="cat-rule"></div>
    <div class="cat-desc">Look'in for your Camp?<br>Caravan and camping<br>accessories.</div>
  </div>
  <div class="abs cat" style="left:517px">
    <svg width="40" height="44" viewBox="0 0 40 44" fill="none" stroke="#333" stroke-width="1.5"><rect x="8" y="4" width="24" height="36"/><path d="M14 14l12 12M26 14l-12 12"/></svg>
    <div class="cat-name">Bed &amp; breakfast</div>
    <div class="cat-desc">Place to eat<br>chinese food, burgers,<br>traditional food</div>
  </div>
  <div class="abs cat" style="left:652px">
    <svg width="40" height="44" viewBox="0 0 40 44" fill="none" stroke="#333" stroke-width="1.5"><path d="M10 40h12M16 40V26M8 14h16c0 8-4 12-8 12s-8-4-8-12zM28 40V18h6v22zM30 18v-12h2v12"/></svg>
    <div class="cat-name">Bar &amp; Drinks</div>
    <div class="cat-desc">Place to catch local news<br>List of Bars &amp; Drinks</div>
  </div>
  <div class="abs cat" style="left:786px">
    <svg width="40" height="44" viewBox="0 0 40 44" fill="none" stroke="#333" stroke-width="1.5"><rect x="8" y="4" width="24" height="36" rx="2"/><rect x="13" y="12" width="14" height="8"/></svg>
    <div class="cat-name">Visitor Guide</div>
    <div class="cat-desc">Here to help you<br>Essentials information<br>were collected for you.</div>
  </div>
</section>

<section class="things">
  <div class="abs ghost" style="top:930px">To do in dorrin</div>
  <h2 class="abs heading" style="top:975px">TOP 10 THINGS TO DO IN DORRIN</h2>

  <svg class="abs arrow" style="left:55px" width="30" height="24" viewBox="0 0 30 24" fill="none" stroke="#666" stroke-width="1.5"><path d="M28 12H2M12 2L2 12l10 10"/></svg>
  <svg class="abs arrow" style="left:1115px" width="30" height="24" viewBox="0 0 30 24" fill="none" stroke="#666" stroke-width="1.5"><path d="M2 12h26M18 2l10 10-10 10"/></svg>

  <article class="abs card" style="left:125px">
    <div class="abs card-img" role="img" aria-label="Aerial photo of a small harbour and beach" style="background:linear-gradient(160deg,#4f8f6a 0%,#5fa3a0 45%,#6fb0b8 70%,#8a9a78 100%)"></div>
    <div class="abs badge">1</div>
    <h3 class="abs card-title">A day trip to Merrowby</h3>
    <p class="abs card-copy">Merrowby is only three miles from Dorrin and offers a gorgeous beach, some lovely shops and restaurants as well as a harbour to rival Dorrin! A bustling, welcoming village - well worth a visit!</p>
    <a class="abs card-link">View Detail ⟶</a>
  </article>

  <article class="abs card" style="left:611px">
    <div class="abs card-img" role="img" aria-label="Photo of a bright craft café interior" style="background:linear-gradient(160deg,#c9c2b8 0%,#c23a4a 40%,#3a5aa8 70%,#d8d0c4 100%)"></div>
    <div class="abs badge">2</div>
    <h3 class="abs card-title">Pippin Creative Cafe</h3>
    <p class="abs card-copy">Newly opened for October 2015 Pippin is a creative Cafe offering a huge range of activities including arts &amp; crafts workshops, children's parties, personalised gifts, T shirt printing, painting, sewing and mask making to name just a few!</p>
    <a class="abs card-link">View Detail ⟶</a>
  </article>

  <a class="abs btn view-all">View all</a>
</section>

<section class="dining">
  <div class="abs ghost" style="top:1610px">Places to Eat</div>
  <h2 class="abs heading" style="top:1656px">DINNER &amp; BREAKFAST</h2>

  <div class="abs dine-img" role="img" aria-label="Photo of a plated dish on a restaurant table with glasses"></div>
  <div class="abs dots"><span></span><span></span></div>

  <article class="abs dine-card">
    <h3 class="abs dine-title">The Brine Room</h3>
    <div class="abs tags">
      <span class="tag">locally sourced ingredients</span><span class="tag">triple cooked chips</span>
      <span class="tag">young couples</span><span class="tag">new venture</span><span class="tag">Crab</span><span class="tag">sea salt</span>
      <span class="tag">peanut butter parfait</span><span class="tag">welsh lamb</span><span class="tag">front of house</span>
    </div>
    <div class="abs dine-copy">
      <p>Selecting the cookware for your kitchen implies a few certain points you should consider: budget, cooking and eating habits, your family size, etc. One of the most essential points in choosing cookware is the material it is made of. Often, such an important detail is simply overlooked or is considered to be minor. In fact, proper understanding of differences between cookware materials will assist you in making the best choice and further on, will help maintain your cookware in a good shape.</p>
      <p>Stainless steel cookware is very common thank to its moderate price and a number of qualities, such as good tensile strength.</p>
    </div>
    <span class="abs pager prev">⟵ PREV</span>
    <span class="abs pager next">NEXT ⟶</span>
  </article>
</section>

<section class="hotels">
  <div class="abs ghost" style="top:2490px">Where to stay</div>
  <h2 class="abs heading" style="top:2533px">BROWSE HOTELS</h2>

  <div class="abs hotel-img" style="left:67px;width:215px;background:linear-gradient(180deg,#b8c0c4,#7d8a8c)" role="img" aria-label="Photo of a white hotel facade"></div>
  <div class="abs hotel-img" style="left:666px;width:215px;background:linear-gradient(180deg,#8fb8e4,#c8ccd0 60%,#6a6e72)" role="img" aria-label="Photo of white town houses on a street corner"></div>
  <div class="abs hotel-img" style="left:920px;width:216px;background:linear-gradient(180deg,#8fc0ea,#6a9cc4 55%,#4a5a6a)" role="img" aria-label="Photo of a blue painted hotel building"></div>

  <article class="abs hotel-card">
    <h3 class="abs hotel-name">The Cliffside Hotel</h3>
    <div class="abs hotel-rule"></div>
    <ul class="abs hotel-info">
      <li><svg width="10" height="10" viewBox="0 0 10 10" fill="#fff"><path d="M2 0l2 2-1 2 3 3 2-1 2 2-2 2C4 10 0 6 0 2z"/></svg>01 555 010 274</li>
      <li><svg width="10" height="8" viewBox="0 0 10 8" fill="#fff"><path d="M0 0h10v8H0zM0 0l5 4 5-4" stroke="#1aa3e8"/></svg>stay@cliffsidedorrin.co.uk</li>
      <li><svg width="10" height="10" viewBox="0 0 10 10"><circle cx="5" cy="5" r="5" fill="#fff"/></svg>http://cliffsidedorrin.co.uk/</li>
    </ul>
    <span class="abs hotel-book">BOOK ONLINE</span>
    <a class="abs btn hotel-detail">VIEW DETAIL</a>
  </article>
</section>

<footer class="abs footer">
  <div class="abs brand"><span class="brand-dot"></span>DORRIN.CO.UK</div>
  <span class="abs copyright">©copyright info dorrin.co.uk</span>
</footer>

</body>
</html>
```